Dwellcraft Brochure

We need a brochure on A4 to show our portfolio and invite people to take up our service offering. This brochure will be mailed to peoples home in the areas that we are targeting. We offer quick house modifications including bathroom and kitchen renovations, disability access, security, extensions and full house renovations as well as design and build services.

Target Market(s)

Home Owners, Occupational Therapists, Retirement village, Medical Centers

Industry/Entity Type

Construction and Design

Requirements
Must have
• Photos and our services listed and an invitation to use them

```html
<!DOCTYPE html>
<html lang="en">
<head>
<meta charset="utf-8">
<title>Dwellcraft Brochure</title>
<link rel="stylesheet" href="https://fonts.googleapis.com/css2?family=Roboto:ital,wght@0,400;0,700;0,900;1,400;1,700;1,900&display=swap">
<style>
  :root {
    --brand-red: #bb1823;
    --ink: #1e1e1e;
    --white: #ffffff;
    --band-light: #e6e4e3;
    --band-mid: #a9a7a7;
    --dark-top: #141416;
    --dark-bottom: #5a5a5c;
    --services-title: #c9c9c9;
    --services-copy: #a8a8aa;
    --logo-grey: #555555;
  }
  * { margin: 0; padding: 0; box-sizing: border-box; }
  html, body { width: 848px; height: 1200px; overflow: hidden; background: var(--white); }
  body { font-family: "Roboto", Arial, sans-serif; color: var(--ink); }
  .brochure { position: relative; width: 848px; height: 1200px; overflow: hidden; background: var(--white); }

  .hero { position: absolute; left: 0; top: 0; width: 848px; height: 466px; }
  .hero svg { position: absolute; inset: 0; }
  .hero-heading { position: absolute; left: 60px; top: 62px; color: var(--white); font-style: italic; font-weight: 900; line-height: 1; }
  .hero-heading .lead { display: block; font-size: 48px; font-weight: 700; letter-spacing: 0.5px; }
  .hero-heading .big { display: block; font-size: 86px; margin-top: 4px; letter-spacing: 1px; }
  .hero-heading .tail { display: block; font-size: 38px; font-weight: 700; line-height: 1.26; margin-top: 10px; }

  .intro-band { position: absolute; left: 0; top: 466px; width: 848px; height: 93px;
    background: linear-gradient(90deg, var(--band-mid) 0%, var(--band-light) 35%, var(--band-light) 65%, var(--band-mid) 100%);
    display: flex; align-items: center; justify-content: center; text-align: center; }
  .intro-band p { font-size: 16.2px; line-height: 21.5px; color: var(--ink); width: 600px; }

  .services-band { position: absolute; left: 0; top: 559px; width: 848px; height: 168px;
    background: linear-gradient(180deg, var(--dark-top) 0%, var(--dark-bottom) 100%); text-align: center; }
  .services-title { margin-top: 16px; font-size: 40px; font-weight: 900; color: var(--services-title); letter-spacing: 1px;
    display: flex; align-items: center; justify-content: center; gap: 14px; }
  .services-title::before, .services-title::after { content: ""; width: 28px; height: 2px; background: var(--services-title); }
  .services-copy { font-size: 14px; line-height: 19px; color: var(--services-copy); margin-top: 6px; }
  .services-copy + .services-copy { margin-top: 8px; }

  .service-photo { position: absolute; width: 236px; height: 210px; }
  .service-photo.renovations { left: 55px; top: 702px; }
  .service-photo.extensions { left: 307px; top: 734px; }
  .service-photo.repairs { left: 558px; top: 700px; }

  .service { position: absolute; text-align: center; font-size: 14.6px; line-height: 17.2px; color: var(--ink); }
  .service h3 { color: var(--brand-red); font-size: 19.5px; font-weight: 700; line-height: 22px; margin-bottom: 2px; }
  .service.renovations { left: 52px; top: 919px; width: 240px; }
  .service.extensions { left: 304px; top: 953px; width: 240px; }
  .service.repairs { left: 556px; top: 919px; width: 240px; }
  .service .highlight { font-weight: 700; margin-top: 17px; }

  .brand-mark { position: absolute; left: 62px; top: 1096px; display: flex; align-items: center; gap: 8px; }
  .brand-mark .square { width: 14px; height: 14px; background: var(--brand-red); }
  .brand-mark .name { font-size: 30px; font-weight: 400; color: var(--brand-red); letter-spacing: 0.5px; }

  .footer-shapes { position: absolute; left: 0; top: 1098px; width: 848px; height: 102px; }
  .cta { position: absolute; left: 332px; top: 1120px; color: var(--white); font-style: italic; font-size: 14.6px; line-height: 20.2px; }
  .cta strong { font-weight: 900; font-size: 17px; letter-spacing: 0.6px; }
  .contact { position: absolute; left: 588px; top: 1121px; list-style: none; color: var(--white); font-size: 15px; font-weight: 700; letter-spacing: 0.3px; }
  .contact li { display: flex; align-items: center; gap: 9px; height: 20.2px; }
  .contact svg { width: 17px; height: 17px; flex: none; }
</style>
</head>
<body>
<main class="brochure">

  <section class="hero">
    <svg width="848" height="466" viewBox="0 0 848 466">
      <defs>
        <linearGradient id="kitchenTone" x1="0" y1="0" x2="0" y2="1">
          <stop offset="0" stop-color="#eeeeef"/>
          <stop offset="0.55" stop-color="#cfcfd0"/>
          <stop offset="0.72" stop-color="#8a7a70"/>
          <stop offset="1" stop-color="#4b3a32"/>
        </linearGradient>
      </defs>
      <rect x="300" y="0" width="548" height="466" fill="url(#kitchenTone)" role="img" aria-label="Photo of a modern renovated kitchen with pendant lights, stone benchtop island and timber stools"/>
      <polygon points="0,0 520,0 345,466 0,466" fill="var(--brand-red)"/>
    </svg>
    <h1 class="hero-heading">
      <span class="lead">Transforming</span>
      <span class="big">HOMES</span>
      <span class="tail">Through Expert<br>Modifications &amp;<br>Renovations</span>
    </h1>
  </section>

  <section class="intro-band">
    <p>We deliver home modifications and renovations that enhance comfort, functionality, and style. Grow your space, modernise your layout, or refresh your home — our expert team delivers quality results from start to finish.</p>
  </section>

  <section class="services-band">
    <h2 class="services-title">OUR SERVICES</h2>
    <p class="services-copy">Whether it’s a full renovation or a smart, space-saving modification,<br>we bring design thinking and craftsmanship to every corner of your home.</p>
    <p class="services-copy">We offer a full range of home improvement services—delivered<br>under one roof by trusted professionals.</p>
  </section>

  <svg class="service-photo renovations" viewBox="0 0 236 210" role="img" aria-label="Photo of a renovated bathroom with freestanding bath and timber vanity">
    <defs>
      <linearGradient id="bathTone" x1="0" y1="0" x2="1" y2="1">
        <stop offset="0" stop-color="#b9b6b2"/><stop offset="0.6" stop-color="#d9d7d4"/><stop offset="1" stop-color="#8f7f70"/>
      </linearGradient>
      <filter id="hexShadow" x="-10%" y="-10%" width="120%" height="120%"><feDropShadow dx="0" dy="2" stdDeviation="2.5" flood-opacity="0.35"/></filter>
    </defs>
    <polygon points="59,5 177,5 231,105 177,205 59,205 5,105" fill="url(#bathTone)" stroke="var(--white)" stroke-width="5" filter="url(#hexShadow)"/>
  </svg>

  <svg class="service-photo extensions" viewBox="0 0 236 210" role="img" aria-label="Photo of an extended open-plan kitchen and dining area with timber table">
    <defs>
      <linearGradient id="diningTone" x1="0" y1="0" x2="0" y2="1">
        <stop offset="0" stop-color="#e8e8e8"/><stop offset="0.4" stop-color="#2f4a48"/><stop offset="0.6" stop-color="#c8833c"/><stop offset="1" stop-color="#2a2522"/>
      </linearGradient>
    </defs>
    <polygon points="59,5 177,5 231,105 177,205 59,205 5,105" fill="url(#diningTone)" stroke="var(--white)" stroke-width="5" filter="url(#hexShadow)"/>
  </svg>

  <svg class="service-photo repairs" viewBox="0 0 236 210" role="img" aria-label="Photo of a kitchen sink with black mixer tap under a window">
    <defs>
      <linearGradient id="sinkTone" x1="0" y1="0" x2="0" y2="1">
        <stop offset="0" stop-color="#a9adab"/><stop offset="0.5" stop-color="#dcdedd"/><stop offset="0.8" stop-color="#2c2c2c"/><stop offset="1" stop-color="#e6e6e6"/>
      </linearGradient>
    </defs>
    <polygon points="59,5 177,5 231,105 177,205 59,205 5,105" fill="url(#sinkTone)" stroke="var(--white)" stroke-width="5" filter="url(#hexShadow)"/>
  </svg>

  <article class="service renovations">
    <h3>Renovations</h3>
    <p>Transform your space with high-quality upgrades including new bathrooms, kitchens, balconies, decks, ramps, fireplaces, pergolas, verandahs, doorways, windows, and accessibility modifications.</p>
  </article>

  <article class="service extensions">
    <h3>Extensions</h3>
    <p>As licensed builders, we manage all structural changes needed to bring your vision to life—whether it’s adding space, reconfiguring layouts, or expanding your home’s potential.</p>
  </article>

  <article class="service repairs">
    <h3>Maintenance &amp; Repairs</h3>
    <p>We quickly and efficiently restore, repair, and replace any defective elements to keep your home safe, functional, and looking its best.</p>
    <p class="highlight">With over 10 years of experience, we deliver high-quality results.</p>
  </article>

  <div class="brand-mark">
    <span class="square"></span>
    <span class="name">DWELLCRAFT</span>
  </div>

  <svg class="footer-shapes" viewBox="0 0 848 102">
    <rect x="0" y="57" width="300" height="45" fill="#3a3a3c"/>
    <polygon points="313,0 848,0 848,102 269,102" fill="var(--brand-red)"/>
  </svg>

  <p class="cta"><strong>CALL US TODAY</strong> and bring our<br>skills and extensive construction<br>experience to your next project.</p>

  <ul class="contact">
    <li>
      <svg viewBox="0 0 24 24"><path fill="#fff" d="M6.6 10.8a15.1 15.1 0 0 0 6.6 6.6l2.2-2.2c.3-.3.7-.4 1-.2 1.1.4 2.3.6 3.6.6.6 0 1 .4 1 1V20c0 .6-.4 1-1 1A17 17 0 0 1 3 4c0-.6.4-1 1-1h3.5c.6 0 1 .4 1 1 0 1.3.2 2.5.6 3.6.1.3 0 .7-.2 1z"/></svg>
      (03) 5550-0142
    </li>
    <li>
      <svg viewBox="0 0 24 24"><path fill="#fff" d="M3 5h18v14H3z"/><path fill="none" stroke="var(--brand-red)" stroke-width="1.8" d="M3.5 6l8.5 7 8.5-7"/></svg>
      info@dwellcraft.com.au
    </li>
    <li>
      <svg viewBox="0 0 24 24"><circle cx="12" cy="12" r="9.5" fill="none" stroke="#fff" stroke-width="2"/><path fill="none" stroke="#fff" stroke-width="1.6" d="M2.5 12h19M12 2.5c-3.5 3.5-3.5 15.5 0 19M12 2.5c3.5 3.5 3.5 15.5 0 19M4.5 7h15M4.5 17h15"/></svg>
      dwellcraft.com.au
    </li>
  </ul>

</main>
</body>
</html>
```